Brand new redesign of Brightwell finance website

I need a new website design that i can advertise a great low interest rate on the front page and capture input application details that will send through to my email address.

some car finance companies will be similar to this would be listed below

tallyfunds.com.au
corelinefinance.com.au
finance715.com.au
wexburyfinance.com.au
finance93.com.au

Reason: I have changed the project to a committed project. all the webpages should have the same format just different content and i want to be able to edit the front page easily to update my interest rates.

Reason: Provide more time for resubmission and submission work

Target Market(s)

Australian Finance market targeting a younger demographic

Industry/Entity Type

Finance

Coding

Coded - Design and coding required

Number of Pages Required

5+ page

Font styles to use
Serif
Sans Serif

Colors
0255a3
ffffff
cedeed

Requirements
Must have
• application capture form
• apply now buttons
• Headline rate front page

```html
<!DOCTYPE html>
<html lang="en">
<head>
<meta charset="utf-8">
<title>Brightwell Finance – Mobile Home</title>
<link href="https://fonts.googleapis.com/css2?family=Open+Sans:wght@400;600;700&family=Roboto+Condensed:wght@400;700&display=swap" rel="stylesheet">
<style>
:root{
  --brand:#0255a3;
  --brand-deep:#1d3f7c;
  --sky:#2b9fd0;
  --button:#0e9ee6;
  --pale:#cedeed;
  --white:#ffffff;
  --ink:#222;
  --footer:#231f22;
  --footer-bar:#1b181a;
  --stage:#eef2f7;
}
*{box-sizing:border-box;margin:0;padding:0}
html,body{width:787px;height:1200px;overflow:hidden;background:var(--stage);font-family:"Open Sans",Arial,sans-serif}
.page{position:absolute;left:193px;top:22px;width:365px;height:1050px;background:var(--white);transform:scale(1.1);transform-origin:0 0;box-shadow:0 4px 18px rgba(20,40,80,.18);overflow:hidden}
.site-header{height:40px;display:flex;align-items:center;justify-content:space-between;padding:0 17px}
.brand{display:flex;align-items:center;gap:6px;color:var(--brand);font-weight:700;font-size:12px;letter-spacing:.3px;text-transform:uppercase}
.brand-dot{width:14px;height:14px;border-radius:50%;background:var(--brand)}
.menu-toggle{width:17px;display:flex;flex-direction:column;gap:3px}
.menu-toggle span{height:2px;background:var(--brand)}
.hero{position:relative;height:175px;color:var(--white);text-align:center}
.hero-photo{position:absolute;inset:0;background:linear-gradient(160deg,#3f9cc4 0%,#2a7bb0 45%,#1d5590 100%)}
.hero-content{position:relative;padding-top:46px}
.hero h1{font-weight:400;font-size:13.5px;letter-spacing:.2px}
.hero .subline{font-size:11px;font-weight:400;margin-top:3px}
.hero .subline b{font-weight:700}
.rates{display:flex;justify-content:center;gap:14px;margin-top:14px;margin-left:-14px}
.rate-label{font-family:"Roboto Condensed",Arial,sans-serif;font-size:10.5px;margin-bottom:4px}
.rate-box{background:var(--white);color:var(--brand);width:73px;height:33px;display:flex;align-items:center;justify-content:center;gap:3px;font-family:"Roboto Condensed",Arial,sans-serif;font-weight:700;font-size:21px}
.rate-box small{font-size:8px;line-height:8px;text-align:left}
.quick-quote{height:69px;background:#1e4f8c;padding:12px 17px 0}
.quick-quote h2{color:var(--white);font-weight:400;font-size:11px;margin-bottom:6px}
.quote-form{display:flex;gap:8px}
.field{height:19px;background:var(--white);font-size:5.5px;color:#777;padding:0 6px;display:flex;align-items:center;justify-content:space-between;width:105px}
.field .caret{width:0;height:0;border:3px solid transparent;border-top:4px solid #777;margin-top:3px}
.btn-apply{flex:1;height:19px;background:var(--button);color:var(--white);font-size:6px;font-weight:600;display:flex;align-items:center;justify-content:center;letter-spacing:.3px}
.services{height:476px;padding-top:25px;text-align:center}
.services h2{font-weight:600;font-size:12.5px;color:var(--ink);margin-bottom:22px}
.service-grid{display:grid;grid-template-columns:161px 161px;gap:10px 9px;padding:0 17px}
.service-tile{position:relative;height:121px}
.service-tile::after{content:"";position:absolute;inset:0;background:linear-gradient(to bottom,transparent 55%,rgba(0,0,0,.55))}
.service-tile span{position:absolute;left:0;right:0;bottom:7px;color:var(--white);font-size:8px;font-weight:600;z-index:1}
.tile-vehicle{background:linear-gradient(135deg,#c9ccd3,#8e97a6 60%,#b5527a)}
.tile-boat{background:linear-gradient(160deg,#9ccbe6,#8f8a73 50%,#3a6e84)}
.tile-home{background:linear-gradient(160deg,#4d7a3c,#d8d8d4 50%,#5d7448)}
.tile-personal{background:linear-gradient(135deg,#9fb6c9,#3f74b3 60%,#c5d6e4)}
.tile-business{background:linear-gradient(160deg,#a8cbea,#3c6ea8 55%,#1d3958)}
.tile-equipment{background:linear-gradient(170deg,#6aa3d8,#c79a2e 55%,#5a4a38)}
.cta{height:121px;background:linear-gradient(100deg,#2b9dc6,#3268a8 70%,#3d5aa0);color:var(--white);text-align:center;padding-top:24px}
.cta h2{font-weight:400;font-size:13.5px}
.cta h2 b{font-weight:700}
.cta p{font-size:6.5px;line-height:8.5px;margin:4px 22px 0}
.btn-outline{display:inline-block;margin-top:14px;border:1px solid var(--white);width:79px;height:19px;line-height:17px;font-size:6.5px;font-weight:600}
.site-footer{height:140px;background:var(--footer);color:var(--white);padding:21px 18px 0}
.footer-top{display:flex;align-items:center;gap:10px}
.footer-top .brand{color:#3b8fd4;border-right:1px solid #3b8fd4;padding-right:10px;height:22px}
.footer-top p{font-size:6.5px;line-height:10px;color:#ddd}
.footer-cols{display:flex;margin-top:23px}
.footer-col{font-size:6.3px;color:#ddd}
.footer-col h3{font-size:8px;font-weight:400;color:var(--white);margin-bottom:10px}
.footer-col.location{width:183px}
.contact-row{display:flex;align-items:center;gap:5px;margin-bottom:10px}
.contact-row svg{width:6px;height:6px}
.footer-bar{height:30px;background:var(--footer-bar);display:flex;align-items:center;justify-content:space-between;padding:0 18px}
.social{display:flex;gap:8px}
.social span{width:15px;height:15px;border-radius:50%;background:#3a3638}
.footer-bar small{font-size:6.3px;color:#ccc}
</style>
</head>
<body>
<main class="page">
  <header class="site-header">
    <div class="brand"><span class="brand-dot"></span>Brightwell Finance</div>
    <div class="menu-toggle" aria-label="Menu"><span></span><span></span><span></span></div>
  </header>

  <section class="hero">
    <div class="hero-photo" role="img" aria-label="Blue-toned photo of a car interior behind the headline"></div>
    <div class="hero-content">
      <h1>WITH A PERSONAL LOAN</h1>
      <p class="subline">RATE STARTING THIS LOW, <b>WHY WAIT ANY LONGER?</b></p>
      <div class="rates">
        <div>
          <div class="rate-label">Home Loan Rate</div>
          <div class="rate-box">4.69<small>%<br>p.a.</small></div>
        </div>
        <div>
          <div class="rate-label">Compare Rate</div>
          <div class="rate-box">4.99<small>%<br>p.a.</small></div>
        </div>
      </div>
    </div>
  </section>

  <section class="quick-quote">
    <h2>Quick Quote</h2>
    <div class="quote-form">
      <div class="field">Purpose of Loan *<span class="caret"></span></div>
      <div class="field">Loan amount *</div>
      <div class="btn-apply">APPLY NOW</div>
    </div>
  </section>

  <section class="services">
    <h2>OUR FINANCIAL SERVICES</h2>
    <div class="service-grid">
      <div class="service-tile tile-vehicle" role="img" aria-label="Photo of two people in a car"><span>VEHICLE LOAN</span></div>
      <div class="service-tile tile-boat" role="img" aria-label="Photo of a sailing boat by a rocky coast"><span>BOAT LOAN</span></div>
      <div class="service-tile tile-home" role="img" aria-label="Photo of a white family house among trees"><span>HOME LOAN</span></div>
      <div class="service-tile tile-personal" role="img" aria-label="Photo of a man in a blue shirt"><span>PERSONAL LOAN</span></div>
      <div class="service-tile tile-business" role="img" aria-label="Photo of glass office towers against the sky"><span>BUSINESS LOAN</span></div>
      <div class="service-tile tile-equipment" role="img" aria-label="Photo of a yellow wheel loader"><span>EQUIPMENT LOAN</span></div>
    </div>
  </section>

  <section class="cta">
    <h2>A <b>SMARTER</b> LOAN. YOU <b>EARNED</b> IT.</h2>
    <p>Dolor sit am consectetuer adipiscing elit, sed diam nonum nibhit euismod tincidunt ut laoreet dolore into amet.</p>
    <span class="btn-outline">APPLY NOW</span>
  </section>

  <footer class="site-footer">
    <div class="footer-top">
      <div class="brand"><span class="brand-dot" style="background:#3b8fd4"></span>Brightwell Finance</div>
      <p>Lorem ipsum dolor sit amet into ametco consectetuer intoin adipiscing elit, sedip diam nonummy nibh.</p>
    </div>
    <div class="footer-cols">
      <div class="footer-col location">
        <h3>LOCATION</h3>
        <p>Unit 4/210 Harbour Rd, Lakeside</p>
      </div>
      <div class="footer-col">
        <h3>CONTACT US</h3>
        <div class="contact-row">
          <svg viewBox="0 0 10 10"><path d="M2 1l2 2-1 1.5c.8 1.5 1.5 2.2 3 3L7.5 6l2 2-1.5 1.5C4 9 1 6 .5 1.5z" fill="#777"/></svg>1300 482 917
          <svg viewBox="0 0 10 10" style="margin-left:10px"><rect x="1" y="3" width="8" height="6" fill="#777"/><rect x="3" y="1" width="4" height="3" fill="#777"/></svg>08 7311 4026
        </div>
        <div class="contact-row">
          <svg viewBox="0 0 10 10"><rect x="1" y="2" width="8" height="6" fill="#777"/><path d="M1 2l4 3 4-3" stroke="#231f22" fill="none"/></svg>hello@brightwellfinance.com
        </div>
      </div>
    </div>
  </footer>
  <div class="footer-bar">
    <div class="social" aria-label="Social links"><span></span><span></span><span></span></div>
    <small>© 2016, brightwellfinance.com. All rights reserved.</small>
  </div>
</main>
</body>
</html>
```